Step and Repeat Backdrop for wedding reception photo booth

Would like to have a Step and Repeat Backdrop (8 foot high by 10 foot wide) that incorporates the wedding logo (attached) and the names Elena and Gavin. Background should be white, and wedding colors are burgundy and gold. Show me creativity :-) I have included some random samples.

```html
<!DOCTYPE html>
<html lang="en">
<head>
<meta charset="utf-8">
<title>Elena &amp; Gavin — Step and Repeat Backdrop</title>
<link rel="stylesheet" href="https://fonts.googleapis.com/css2?family=Cinzel:wght@500&display=swap">
<style>
  :root {
    --page: #ececec;
    --backdrop: #ffffff;
    --burgundy: #7d0f1a;
    --gold: #b8923f;
    --gold-light: #d4b26a;
    --tile-w: 118px;
    --row-h: 114px;
  }
  * { box-sizing: border-box; margin: 0; padding: 0; }
  html, body {
    width: 1200px; height: 1200px; overflow: hidden;
    background: var(--page);
  }
  .canvas {
    position: relative; width: 1200px; height: 1200px;
    display: flex; align-items: center; justify-content: center;
  }
  .backdrop {
    position: relative; width: 1160px; height: 898px;
    background: var(--backdrop); overflow: hidden;
    padding-top: 3px;
  }
  .row {
    display: flex; height: var(--row-h); flex-wrap: nowrap;
  }
  .row--a { margin-left: -58px; }
  .row--b { margin-left: -19px; }
  .row--c { margin-left: 21px; }
  .tile {
    flex: 0 0 var(--tile-w); height: 90px;
    display: flex; flex-direction: column; align-items: center; justify-content: center; gap: 8px;
  }
  .tile__dot {
    width: 52px; height: 52px; border-radius: 50%;
    border: 2px solid var(--gold);
  }
  .tile--burgundy .tile__dot { background: var(--burgundy); }
  .tile--white .tile__dot { background: var(--backdrop); }
  .tile__name {
    font-family: "Cinzel", serif; font-weight: 500;
    font-size: 10px; letter-spacing: 0.5px; color: var(--gold);
    white-space: nowrap;
  }
  .tile--blank { visibility: hidden; }
  .feature {
    position: absolute; left: 295px; top: 324px; width: 570px; height: 230px;
    display: flex; flex-direction: column; align-items: center; justify-content: center; gap: 22px;
  }
  .feature__dot {
    width: 130px; height: 130px; border-radius: 50%;
    border: 3px solid var(--gold);
  }
  .feature__name {
    font-family: "Cinzel", serif; font-weight: 500;
    font-size: 30px; letter-spacing: 3px; color: var(--gold);
  }
</style>
</head>
<body>
<main class="canvas">
  <section class="backdrop" aria-label="Step and repeat backdrop">
    <div class="row row--a">
      <div class="tile tile--burgundy"><span class="tile__dot"></span><span class="tile__name">ELENA &amp; GAVIN</span></div>
      <div class="tile tile--white"><span class="tile__dot"></span><span class="tile__name">ELENA &amp; GAVIN</span></div>
      <div class="tile tile--burgundy"><span class="tile__dot"></span><span class="tile__name">ELENA &amp; GAVIN</span></div>
      <div class="tile tile--white"><span class="tile__dot"></span><span class="tile__name">ELENA &amp; GAVIN</span></div>
      <div class="tile tile--burgundy"><span class="tile__dot"></span><span class="tile__name">ELENA &amp; GAVIN</span></div>
      <div class="tile tile--white"><span class="tile__dot"></span><span class="tile__name">ELENA &amp; GAVIN</span></div>
      <div class="tile tile--burgundy"><span class="tile__dot"></span><span class="tile__name">ELENA &amp; GAVIN</span></div>
      <div class="tile tile--white"><span class="tile__dot"></span><span class="tile__name">ELENA &amp; GAVIN</span></div>
      <div class="tile tile--burgundy"><span class="tile__dot"></span><span class="tile__name">ELENA &amp; GAVIN</span></div>
      <div class="tile tile--white"><span class="tile__dot"></span><span class="tile__name">ELENA &amp; GAVIN</span></div>
      <div class="tile tile--burgundy"><span class="tile__dot"></span><span class="tile__name">ELENA &amp; GAVIN</span></div>
    </div>
    <div class="row row--b">
      <div class="tile tile--white"><span class="tile__dot"></span><span class="tile__name">ELENA &amp; GAVIN</span></div>
      <div class="tile tile--burgundy"><span class="tile__dot"></span><span class="tile__name">ELENA &amp; GAVIN</span></div>
      <div class="tile tile--white"><span class="tile__dot"></span><span class="tile__name">ELENA &amp; GAVIN</span></div>
      <div class="tile tile--burgundy"><span class="tile__dot"></span><span class="tile__name">ELENA &amp; GAVIN</span></div>
      <div class="tile tile--white"><span class="tile__dot"></span><span class="tile__name">ELENA &amp; GAVIN</span></div>
      <div class="tile tile--burgundy"><span class="tile__dot"></span><span class="tile__name">ELENA &amp; GAVIN</span></div>
      <div class="tile tile--white"><span class="tile__dot"></span><span class="tile__name">ELENA &amp; GAVIN</span></div>
      <div class="tile tile--burgundy"><span class="tile__dot"></span><span class="tile__name">ELENA &amp; GAVIN</span></div>
      <div class="tile tile--white"><span class="tile__dot"></span><span class="tile__name">ELENA &amp; GAVIN</span></div>
      <div class="tile tile--burgundy"><span class="tile__dot"></span><span class="tile__name">ELENA &amp; GAVIN</span></div>
      <div class="tile tile--white"><span class="tile__dot"></span><span class="tile__name">ELENA &amp; GAVIN</span></div>
    </div>
    <div class="row row--c">
      <div class="tile tile--burgundy"><span class="tile__dot"></span><span class="tile__name">ELENA &amp; GAVIN</span></div>
      <div class="tile tile--white"><span class="tile__dot"></span><span class="tile__name">ELENA &amp; GAVIN</span></div>
      <div class="tile tile--burgundy"><span class="tile__dot"></span><span class="tile__name">ELENA &amp; GAVIN</span></div>
      <div class="tile tile--white"><span class="tile__dot"></span><span class="tile__name">ELENA &amp; GAVIN</span></div>
      <div class="tile tile--burgundy"><span class="tile__dot"></span><span class="tile__name">ELENA &amp; GAVIN</span></div>
      <div class="tile tile--white"><span class="tile__dot"></span><span class="tile__name">ELENA &amp; GAVIN</span></div>
      <div class="tile tile--burgundy"><span class="tile__dot"></span><span class="tile__name">ELENA &amp; GAVIN</span></div>
      <div class="tile tile--white"><span class="tile__dot"></span><span class="tile__name">ELENA &amp; GAVIN</span></div>
      <div class="tile tile--burgundy"><span class="tile__dot"></span><span class="tile__name">ELENA &amp; GAVIN</span></div>
      <div class="tile tile--white"><span class="tile__dot"></span><span class="tile__name">ELENA &amp; GAVIN</span></div>
      <div class="tile tile--burgundy"><span class="tile__dot"></span><span class="tile__name">ELENA &amp; GAVIN</span></div>
    </div>
    <div class="row row--a">
      <div class="tile tile--burgundy"><span class="tile__dot"></span><span class="tile__name">ELENA &amp; GAVIN</span></div>
      <div class="tile tile--white"><span class="tile__dot"></span><span class="tile__name">ELENA &amp; GAVIN</span></div>
      <div class="tile tile--burgundy"><span class="tile__dot"></span><span class="tile__name">ELENA &amp; GAVIN</span></div>
      <div class="tile tile--blank"></div>
      <div class="tile tile--blank"></div>
      <div class="tile tile--blank"></div>
      <div class="tile tile--blank"></div>
      <div class="tile tile--blank"></div>
      <div class="tile tile--burgundy"><span class="tile__dot"></span><span class="tile__name">ELENA &amp; GAVIN</span></div>
      <div class="tile tile--white"><span class="tile__dot"></span><span class="tile__name">ELENA &amp; GAVIN</span></div>
      <div class="tile tile--burgundy"><span class="tile__dot"></span><span class="tile__name">ELENA &amp; GAVIN</span></div>
    </div>
    <div class="row row--b">
      <div class="tile tile--white"><span class="tile__dot"></span><span class="tile__name">ELENA &amp; GAVIN</span></div>
      <div class="tile tile--burgundy"><span class="tile__dot"></span><span class="tile__name">ELENA &amp; GAVIN</span></div>
      <div class="tile tile--white"><span class="tile__dot"></span><span class="tile__name">ELENA &amp; GAVIN</span></div>
      <div class="tile tile--blank"></div>
      <div class="tile tile--blank"></div>
      <div class="tile tile--blank"></div>
      <div class="tile tile--blank"></div>
      <div class="tile tile--burgundy"><span class="tile__dot"></span><span class="tile__name">ELENA &amp; GAVIN</span></div>
      <div class="tile tile--white"><span class="tile__dot"></span><span class="tile__name">ELENA &amp; GAVIN</span></div>
      <div class="tile tile--burgundy"><span class="tile__dot"></span><span class="tile__name">ELENA &amp; GAVIN</span></div>
      <div class="tile tile--white"><span class="tile__dot"></span><span class="tile__name">ELENA &amp; GAVIN</span></div>
    </div>
    <div class="row row--c">
      <div class="tile tile--burgundy"><span class="tile__dot"></span><span class="tile__name">ELENA &amp; GAVIN</span></div>
      <div class="tile tile--white"><span class="tile__dot"></span><span class="tile__name">ELENA &amp; GAVIN</span></div>
      <div class="tile tile--burgundy"><span class="tile__dot"></span><span class="tile__name">ELENA &amp; GAVIN</span></div>
      <div class="tile tile--white"><span class="tile__dot"></span><span class="tile__name">ELENA &amp; GAVIN</span></div>
      <div class="tile tile--burgundy"><span class="tile__dot"></span><span class="tile__name">ELENA &amp; GAVIN</span></div>
      <div class="tile tile--white"><span class="tile__dot"></span><span class="tile__name">ELENA &amp; GAVIN</span></div>
      <div class="tile tile--burgundy"><span class="tile__dot"></span><span class="tile__name">ELENA &amp; GAVIN</span></div>
      <div class="tile tile--white"><span class="tile__dot"></span><span class="tile__name">ELENA &amp; GAVIN</span></div>
      <div class="tile tile--burgundy"><span class="tile__dot"></span><span class="tile__name">ELENA &amp; GAVIN</span></div>
      <div class="tile tile--white"><span class="tile__dot"></span><span class="tile__name">ELENA &amp; GAVIN</span></div>
      <div class="tile tile--burgundy"><span class="tile__dot"></span><span class="tile__name">ELENA &amp; GAVIN</span></div>
    </div>
    <div class="row row--a">
      <div class="tile tile--burgundy"><span class="tile__dot"></span><span class="tile__name">ELENA &amp; GAVIN</span></div>
      <div class="tile tile--white"><span class="tile__dot"></span><span class="tile__name">ELENA &amp; GAVIN</span></div>
      <div class="tile tile--burgundy"><span class="tile__dot"></span><span class="tile__name">ELENA &amp; GAVIN</span></div>
      <div class="tile tile--white"><span class="tile__dot"></span><span class="tile__name">ELENA &amp; GAVIN</span></div>
      <div class="tile tile--burgundy"><span class="tile__dot"></span><span class="tile__name">ELENA &amp; GAVIN</span></div>
      <div class="tile tile--white"><span class="tile__dot"></span><span class="tile__name">ELENA &amp; GAVIN</span></div>
      <div class="tile tile--burgundy"><span class="tile__dot"></span><span class="tile__name">ELENA &amp; GAVIN</span></div>
      <div class="tile tile--white"><span class="tile__dot"></span><span class="tile__name">ELENA &amp; GAVIN</span></div>
      <div class="tile tile--burgundy"><span class="tile__dot"></span><span class="tile__name">ELENA &amp; GAVIN</span></div>
      <div class="tile tile--white"><span class="tile__dot"></span><span class="tile__name">ELENA &amp; GAVIN</span></div>
      <div class="tile tile--burgundy"><span class="tile__dot"></span><span class="tile__name">ELENA &amp; GAVIN</span></div>
    </div>
    <div class="row row--b">
      <div class="tile tile--white"><span class="tile__dot"></span><span class="tile__name">ELENA &amp; GAVIN</span></div>
      <div class="tile tile--burgundy"><span class="tile__dot"></span><span class="tile__name">ELENA &amp; GAVIN</span></div>
      <div class="tile tile--white"><span class="tile__dot"></span><span class="tile__name">ELENA &amp; GAVIN</span></div>
      <div class="tile tile--burgundy"><span class="tile__dot"></span><span class="tile__name">ELENA &amp; GAVIN</span></div>
      <div class="tile tile--white"><span class="tile__dot"></span><span class="tile__name">ELENA &amp; GAVIN</span></div>
      <div class="tile tile--burgundy"><span class="tile__dot"></span><span class="tile__name">ELENA &amp; GAVIN</span></div>
      <div class="tile tile--white"><span class="tile__dot"></span><span class="tile__name">ELENA &amp; GAVIN</span></div>
      <div class="tile tile--burgundy"><span class="tile__dot"></span><span class="tile__name">ELENA &amp; GAVIN</span></div>
      <div class="tile tile--white"><span class="tile__dot"></span><span class="tile__name">ELENA &amp; GAVIN</span></div>
      <div class="tile tile--burgundy"><span class="tile__dot"></span><span class="tile__name">ELENA &amp; GAVIN</span></div>
      <div class="tile tile--white"><span class="tile__dot"></span><span class="tile__name">ELENA &amp; GAVIN</span></div>
    </div>

    <div class="feature">
      <span class="feature__dot"></span>
      <span class="feature__name">ELENA &amp; GAVIN</span>
    </div>
  </section>
</main>
</body>
</html>
```